Brightmoor Partners Branding Revamp

We are a consulting company, looking for a way to display and promote our brand. We have 2 sides to the business- Brightmoor (financial) and Partners (cyber security). The financial side products relate to business necessities: card processing, website design/hosting/maintenance, VoIP phone systems. The cyber security side promotes a bundled package of 4 solutions: network vulnerability scan, dark web scan, anti-ransomeware/malware software, and image-level backups. We want people to understand that partnering with Brightmoor Partners gives them “Solid Ground, Clear View” (tagline). Current badge and logos uploaded.

Target Market(s)

Small businesses

Contact Information for Business Card

Lena Marwick, Vice President, lena@brightmoorpartners.example, 555-806-1937, www.brightmoorpartners.example

Requirements
Nice to have
• I do prefer the darker background for front and back

```html
<!DOCTYPE html>
<html lang="en">
<head>
<meta charset="utf-8">
<title>Brightmoor Partners — Business Card</title>
<link href="https://fonts.googleapis.com/css2?family=Source+Sans+3:wght@400;600;700&display=swap" rel="stylesheet">
<style>
  :root {
    --backdrop: #e4e4e4;
    --card: #232323;
    --red: #e0232a;
    --red-deep: #8e1116;
    --white: #ffffff;
    --text: #f2f2f2;
  }
  * { margin: 0; padding: 0; box-sizing: border-box; }
  html, body {
    width: 1200px; height: 960px; overflow: hidden;
    background: var(--backdrop);
    font-family: "Source Sans 3", "Source Sans Pro", Arial, sans-serif;
  }
  .canvas { position: relative; width: 1200px; height: 960px; }
  .card {
    position: absolute; left: 299px; width: 598px; height: 340px;
    background: var(--card); overflow: hidden;
  }
  .card--front { top: 119px; }
  .card--back { top: 513px; }

  .brand-accent { position: absolute; top: 0; height: 340px; width: 146px; }
  .card--front .brand-accent { left: 0; background: linear-gradient(100deg, var(--red) 0%, var(--red-deep) 60%, rgba(142,17,22,0) 100%); }
  .card--back .brand-accent { right: 0; background: linear-gradient(280deg, var(--red) 0%, var(--red-deep) 60%, rgba(142,17,22,0) 100%); }

  .wordmark {
    color: var(--white); font-weight: 600; text-transform: uppercase;
    letter-spacing: 0.22em; line-height: 1.15; text-align: center;
  }
  .card--front .wordmark {
    position: absolute; left: 180px; width: 384px; top: 132px; font-size: 34px;
  }
  .tagline {
    position: absolute; left: 180px; width: 384px; top: 282px;
    text-align: center; color: var(--white); font-weight: 700; font-size: 17px;
    text-transform: uppercase;
  }

  .card--back .wordmark {
    position: absolute; left: 38px; top: 108px; width: 214px; font-size: 22px; letter-spacing: 0.2em;
  }
  .marker { position: absolute; left: 0; top: 185px; }
  .person { position: absolute; left: 39px; top: 182px; }
  .person__name { color: var(--red); font-weight: 600; font-size: 20px; line-height: 1.2; }
  .person__title { color: var(--text); font-size: 15.5px; margin-top: 1px; }
  .contacts { position: absolute; left: 39px; top: 247px; list-style: none; }
  .contacts li {
    display: flex; align-items: center; gap: 5px;
    color: var(--text); font-size: 15.5px; line-height: 20px;
  }
  .contacts svg { width: 13px; height: 13px; flex: none; }
</style>
</head>
<body>
<div class="canvas">
  <section class="card card--front">
    <div class="brand-accent" role="img" aria-label="Red brand accent graphic"></div>
    <div class="wordmark">Brightmoor<br>Partners</div>
    <p class="tagline">Solid ground, clear view</p>
  </section>

  <section class="card card--back">
    <div class="wordmark">Brightmoor<br>Partners</div>
    <svg class="marker" width="20" height="24" viewBox="0 0 20 24"><polygon points="0,0 20,12 0,24" fill="var(--red)"/></svg>
    <div class="person">
      <p class="person__name">Lena Marwick</p>
      <p class="person__title">Vice President</p>
    </div>
    <ul class="contacts">
      <li>
        <svg viewBox="0 0 16 16"><path d="M3.5 1.5l2.5 3-1.5 1.5c.8 2 2.5 3.7 4.5 4.5L10.5 9l3 2.5-1.5 2.5C7 14 2 9 2 3.5z" fill="var(--red)"/></svg>
        555-806-1937
      </li>
      <li>
        <svg viewBox="0 0 16 16"><rect x="1" y="3" width="14" height="10" fill="none" stroke="var(--red)" stroke-width="1.6"/><path d="M1 3l7 6 7-6" fill="none" stroke="var(--red)" stroke-width="1.6"/></svg>
        lena@brightmoorpartners.example
      </li>
      <li>
        <svg viewBox="0 0 16 16"><circle cx="8" cy="8" r="6.5" fill="none" stroke="var(--red)" stroke-width="1.4"/><ellipse cx="8" cy="8" rx="2.8" ry="6.5" fill="none" stroke="var(--red)" stroke-width="1.2"/><path d="M1.5 8h13" stroke="var(--red)" stroke-width="1.2"/></svg>
        www.brightmoorpartners.example
      </li>
    </ul>
    <div class="brand-accent" role="img" aria-label="Red brand accent graphic"></div>
  </section>
</div>
</body>
</html>
```